Trade Show booth design

I need the following designs for my trade booth:
1. backboard design 3m Wx2mH
2. Tressle table, tablecloth front panel design 1800W x 740mmH
3. Pop-up banner. I have included our logos and some design content ideas:
Headline:
"Cleaner Classrooms. Safer Schools."
Subheadline:
"Specialist Cleaning Solutions for Education Facilities"
Key Points to Grab Attention:
Healthy Environments: Create hygienic, safe learning spaces for students and staff with our expert cleaning services.
Tailored to Your Needs: Custom cleaning plans for classrooms, labs, libraries, and sports facilities.
Affordable Excellence: Premium results without premium costs – tailored plans mean you only pay for what you need.
Safety First: All staff are trained, highly vetted, and hold current Working with Children Checks (WWCC).
Eco-Conscious Cleaning: Using non-toxic, eco-friendly products certified for health and safety.
What Schools Really Need:
Reliability: Consistent, high-quality cleaning from a trusted provider.
Cost-Effectiveness: Solutions that fit tight budgets while maintaining high standards.
Expertise: Over 30 years of experience in education facility cleaning.
Disinfection Services: Focus on high-touch areas to reduce the spread of germs and ensure peace of mind.
Visual Elements:
Images of bright, clean classrooms, a happy teacher welcoming students, or students collaborating in a spotless library.
Icons representing safety (shield), hygiene (sparkling star), and eco-friendliness (leaf).
Your logo with the tagline: "Trusted by Queensland Schools Since 1995."
Call-to-Action:
"Visit us to discuss your school’s cleaning needs and book a FREE consultation."
Include contact details: Phone: 1300 648 319 | Website: www.vardenmop.com.au
Target Market(s)
Education sector
Industry/Entity Type
Commercial Cleaning
Font styles to use
Other font styles liked:
- Montserrat
Look and feel

```html
<!DOCTYPE html>
<html lang="en">
<head>
<meta charset="utf-8">
<title>Vardenmop – Trade Show Booth Set</title>
<link rel="stylesheet" href="https://fonts.googleapis.com/css2?family=Montserrat:wght@500;600&family=Roboto+Condensed:wght@300;400;700&family=Roboto:wght@400;500&display=swap">
<style>
  :root {
    --navy: #1f3a60;
    --navy-deep: #142a4a;
    --navy-mid: #2b4f7e;
    --band-blue: #3d6597;
    --slate: #3c5878;
    --paper: #f3f4f6;
    --paper-shade: #e3e6ea;
    --ice: #c9d3de;
    --photo-teal: #8fcdbd;
    --photo-light: #eef1f0;
    --white: #ffffff;
  }
  html, body {
    margin: 0;
    width: 1200px;
    height: 2669px;
    overflow: hidden;
    background: var(--white);
  }
  .canvas { position: relative; width: 1200px; height: 2669px; }
  .piece { position: absolute; display: block; }
  .backboard { left: 125px; top: 200px; width: 925px; height: 650px; }
  .table-panel { left: 190px; top: 695px; width: 297px; height: 330px; }
  .popup-banner { left: 320px; top: 1100px; width: 432px; height: 1245px; }
  .brand-name { font-family: "Montserrat", sans-serif; font-weight: 600; }
  .label { font-family: "Roboto", sans-serif; font-weight: 400; }
  .head-light { font-family: "Roboto Condensed", sans-serif; font-weight: 300; }
  .head-bold { font-family: "Roboto Condensed", sans-serif; font-weight: 700; }
  .body-copy { font-family: "Roboto", sans-serif; font-weight: 400; }
  .phone { font-family: "Roboto", sans-serif; font-weight: 500; }
  .web { font-family: "Roboto", sans-serif; font-weight: 400; }
  .defs { position: absolute; width: 0; height: 0; }
</style>
</head>
<body>
<svg class="defs" aria-hidden="true">
  <defs>
    <linearGradient id="paperGrad" x1="0" y1="0" x2="1" y2="1">
      <stop offset="0" stop-color="#e9ebef"/>
      <stop offset="0.5" stop-color="#f7f8f9"/>
      <stop offset="1" stop-color="#eceef1"/>
    </linearGradient>
    <linearGradient id="navyGrad" x1="0" y1="0" x2="1" y2="1">
      <stop offset="0" stop-color="#2b4f7e"/>
      <stop offset="1" stop-color="#142a4a"/>
    </linearGradient>
    <linearGradient id="photoGrad" x1="0" y1="0" x2="0" y2="1">
      <stop offset="0" stop-color="#eef1f0"/>
      <stop offset="0.45" stop-color="#d9e6e2"/>
      <stop offset="1" stop-color="#8fcdbd"/>
    </linearGradient>
    <symbol id="icon-shield" viewBox="-40 -40 80 80">
      <path d="M0,-34 L28,-24 C28,6 18,24 0,36 C-18,24 -28,6 -28,-24 Z" fill="none" stroke="#c9d3de" stroke-width="5"/>
      <path d="M0,-24 L19,-17 C19,4 12,17 0,26 C-12,17 -19,4 -19,-17 Z" fill="#c9d3de"/>
    </symbol>
    <symbol id="icon-sparkle" viewBox="-40 -40 80 80">
      <g fill="none" stroke="#ffffff" stroke-width="3" stroke-linejoin="round">
        <path d="M0,-22 Q2,-2 20,0 Q2,2 0,22 Q-2,2 -20,0 Q-2,-2 0,-22 Z"/>
        <path d="M-24,-30 Q-23,-23 -16,-22 Q-23,-21 -24,-14 Q-25,-21 -32,-22 Q-25,-23 -24,-30 Z"/>
        <path d="M24,14 Q25,22 33,23 Q25,24 24,32 Q23,24 15,23 Q23,22 24,14 Z"/>
      </g>
    </symbol>
    <symbol id="icon-leaf" viewBox="-40 -40 80 80">
      <path d="M-22,28 C-32,-6 -2,-30 30,-30 C32,2 10,28 -22,28 Z" fill="#c9d3de"/>
      <path d="M-28,34 L18,-16" stroke="#1f3a60" stroke-width="3" stroke-linecap="round"/>
    </symbol>
  </defs>
</svg>

<main class="canvas">

  <!-- Backboard 3m x 2m -->
  <svg class="piece backboard" viewBox="0 0 925 650" role="img" aria-label="Backboard: specialist cleaning solutions for education facilities">
    <defs>
      <clipPath id="boardClip"><rect x="25" y="0" width="875" height="650"/></clipPath>
    </defs>
    <rect class="board-paper" width="925" height="650" fill="url(#paperGrad)"/>
    <rect class="board-blue-field" x="0" y="325" width="925" height="325" fill="url(#navyGrad)"/>
    <rect class="board-band" x="0" y="552" width="925" height="43" fill="var(--band-blue)"/>
    <rect class="board-footer" x="0" y="595" width="925" height="55" fill="var(--paper)"/>
    <rect class="board-edge" x="0" y="0" width="25" height="650" fill="var(--navy)"/>
    <rect class="board-edge" x="900" y="0" width="25" height="650" fill="var(--navy)"/>
    <g class="board-photo" clip-path="url(#boardClip)">
      <circle cx="190" cy="300" r="216" fill="var(--paper)"/>
      <circle cx="190" cy="300" r="200" fill="url(#photoGrad)" role="img" aria-label="Photo of a bright, clean classroom with teal floor and desks"/>
    </g>

    <text class="brand-name" x="520" y="150" font-size="58" fill="var(--navy)" text-anchor="middle">vardenmop</text>
    <circle class="brand-dot" cx="770" cy="128" r="30" fill="var(--navy)"/>

    <g class="value-labels label" font-size="24" fill="var(--navy)" text-anchor="middle">
      <text x="528" y="232">Safety</text>
      <text x="663" y="230">Hygiene</text>
      <text x="790" y="228">eco</text>
    </g>
    <g class="value-icons">
      <circle cx="520" cy="320" r="72" fill="var(--paper)"/>
      <circle cx="520" cy="320" r="63" fill="var(--navy)"/>
      <use href="#icon-shield" x="480" y="280" width="80" height="80"/>
      <circle cx="658" cy="320" r="72" fill="var(--paper)"/>
      <circle cx="658" cy="320" r="63" fill="var(--navy)"/>
      <use href="#icon-sparkle" x="618" y="280" width="80" height="80"/>
      <circle cx="790" cy="320" r="72" fill="var(--paper)"/>
      <circle cx="790" cy="320" r="63" fill="var(--navy)"/>
      <use href="#icon-leaf" x="750" y="280" width="80" height="80"/>
    </g>

    <g class="headline" fill="var(--white)" text-anchor="middle">
      <text class="head-light" x="650" y="434" font-size="26">SPECIALIST</text>
      <text class="head-bold" x="650" y="478" font-size="44">CLEANING SOLUTIONS</text>
      <text class="head-light" x="652" y="516" font-size="27">FOR EDUCATION FACILITIES</text>
    </g>
    <text class="web" x="368" y="579" font-size="15" letter-spacing="2.5" fill="var(--white)">www.vardenmop.com.au</text>
    <text class="phone" x="872" y="581" font-size="19" fill="var(--white)" text-anchor="end"><tspan font-weight="400" font-size="17">CALL US NOW!  </tspan>1300 648 319</text>
    <text class="body-copy" x="366" y="614" font-size="13.5" fill="var(--navy-deep)">Visit us to discuss your school’s cleaning needs and book a FREE consultation</text>
  </svg>

  <!-- Trestle table front panel -->
  <svg class="piece table-panel" viewBox="0 0 297 330" role="img" aria-label="Table front panel">
    <rect width="297" height="330" rx="4" fill="url(#navyGrad)"/>
    <rect width="297" height="12" fill="var(--navy-deep)"/>
    <circle cx="48" cy="164" r="13" fill="var(--white)"/>
    <text class="brand-name" x="72" y="175" font-size="32" fill="var(--white)">vardenmop</text>
  </svg>

  <!-- Pop-up banner -->
  <svg class="piece popup-banner" viewBox="0 0 432 1245" role="img" aria-label="Pop-up banner: specialist cleaning solutions for education facilities">
    <defs>
      <clipPath id="bannerClip"><rect width="432" height="1245"/></clipPath>
    </defs>
    <rect class="banner-paper" width="432" height="1245" fill="url(#paperGrad)"/>
    <polygon class="banner-shade" points="432,130 432,480 260,520" fill="var(--paper-shade)"/>
    <path class="banner-blue-field" d="M432,470 L300,610 L0,980 L0,1245 L432,1245 Z" fill="url(#navyGrad)"/>

    <text class="brand-name" x="190" y="114" font-size="38" fill="var(--slate)" text-anchor="middle">vardenmop</text>
    <circle class="brand-dot" cx="335" cy="101" r="18" fill="var(--slate)"/>

    <g class="headline" fill="var(--slate)" text-anchor="middle">
      <text class="head-light" x="216" y="235" font-size="46">SPECIALIST</text>
      <text class="head-bold" x="216" y="307" font-size="74">CLEANING</text>
      <text class="head-bold" x="216" y="382" font-size="74">SOLUTIONS</text>
      <text class="head-light" x="216" y="432" font-size="35">FOR EDUCATION FACILITIES</text>
    </g>

    <g class="banner-photo" clip-path="url(#bannerClip)">
      <circle cx="90" cy="735" r="262" fill="var(--paper)"/>
      <circle cx="90" cy="735" r="245" fill="url(#photoGrad)" role="img" aria-label="Photo of a bright, clean classroom with teal floor and desks"/>
    </g>

    <g class="value-icons">
      <circle cx="258" cy="565" r="55" fill="var(--paper)"/>
      <circle cx="258" cy="565" r="48" fill="var(--navy)"/>
      <text class="label" x="258" y="545" font-size="14" fill="var(--white)" text-anchor="middle">Safety</text>
      <use href="#icon-shield" x="232" y="550" width="52" height="52"/>
      <circle cx="318" cy="740" r="55" fill="var(--paper)"/>
      <circle cx="318" cy="740" r="48" fill="var(--navy)"/>
      <text class="label" x="318" y="720" font-size="14" fill="var(--white)" text-anchor="middle">Hygiene</text>
      <use href="#icon-sparkle" x="292" y="725" width="52" height="52"/>
      <circle cx="260" cy="905" r="55" fill="var(--paper)"/>
      <circle cx="260" cy="905" r="48" fill="var(--navy)"/>
      <text class="label" x="260" y="885" font-size="14" fill="var(--white)" text-anchor="middle">eco</text>
      <use href="#icon-leaf" x="234" y="890" width="52" height="52"/>
    </g>

    <g class="cta" fill="var(--white)" text-anchor="middle">
      <text class="body-copy" x="216" y="1030" font-size="18">Visit us to discuss your school’s cleaning needs</text>
      <text class="body-copy" x="216" y="1056" font-size="18">and book a FREE consultation</text>
      <text class="phone" x="216" y="1128" font-size="26"><tspan font-weight="400" font-size="22">CALL US NOW!  </tspan>1300 648 319</text>
      <text class="web" x="216" y="1172" font-size="20" letter-spacing="4">www.vardenmop.com.au</text>
    </g>
  </svg>

</main>
</body>
</html>
```